Business Podcaster needs a sexy book cover design for upcoming book launch

I'm launching a book called Find Your Mentor: How to fast-track your career by contacting, hearing back from, and making a lasting mark on the leaders you look up to most. It would be cool to have maybe a band of heroes or a single hero or something on the cover, then I'll need the spine designed, as well as the back cover which would be mostly just quotes about the book from other prominent people.

I dont want to extend it. I want to shorten it. Can I do that?

```html
<!DOCTYPE html>
<html lang="en">
<head>
<meta charset="utf-8">
<title>Find Your Mentor – Book Cover Spread</title>
<link rel="stylesheet" href="https://fonts.googleapis.com/css2?family=Dosis:wght@300;400;500;600&family=Signika:wght@400&family=Open+Sans:wght@300;400;800&display=swap">
<style>
  :root {
    --page: #ffffff;
    --back-grey: #dcdddf;
    --accent-blue: #52a1d9;
    --title-blue: #3b93d6;
    --ink: #1f1f22;
    --white: #ffffff;
    --sky-top: #7f929f;
    --sky-mid: #d9dcd9;
    --glow: #f2d27a;
    --ground: #2a2616;
  }
  * { margin: 0; padding: 0; box-sizing: border-box; }
  html, body { width: 1200px; height: 1200px; overflow: hidden; background: var(--page); }
  .spread { position: relative; width: 1200px; height: 1200px; }

  .back-cover {
    position: absolute; left: 0; top: 134px; width: 566px; height: 904px;
    background: var(--back-grey);
  }
  .back-copy {
    position: absolute; left: 68px; top: 66px; width: 437px;
    font-family: "Dosis", sans-serif; font-weight: 400; font-size: 18.5px;
    line-height: 32.6px; color: var(--ink); text-align: justify;
  }
  .back-copy .lead { font-size: 34px; font-weight: 400; }
  .author-band {
    position: absolute; left: 0; top: 556px; width: 566px; height: 169px;
    background: var(--accent-blue); color: var(--white);
    font-family: "Dosis", sans-serif;
  }
  .author-band h2 {
    font-weight: 400; font-size: 23px; text-align: center;
    margin-top: 17px; margin-left: 26px;
  }
  .author-band p {
    width: 439px; margin: 6px 0 0 70px; font-size: 15.5px; font-weight: 300;
    line-height: 19.6px; text-align: justify;
  }
  .barcode-area {
    position: absolute; left: 358px; top: 749px; width: 186px; height: 118px;
    background: var(--white);
  }

  .spine {
    position: absolute; left: 566px; top: 134px; width: 66px; height: 904px;
    background: var(--accent-blue);
  }
  .spine-text {
    position: absolute; left: 50%; white-space: nowrap;
    transform-origin: 0 0; transform: rotate(90deg) translateY(-50%);
    line-height: 1;
  }
  .spine-title {
    top: 48px; font-family: "Dosis", sans-serif; font-weight: 400;
    font-size: 39px; color: var(--ink); letter-spacing: 1px;
  }
  .spine-title .accent { color: var(--white); }
  .spine-author {
    top: 586px; font-family: "Open Sans", sans-serif; font-size: 29px;
    color: var(--white); letter-spacing: 2px;
  }
  .spine-author .first { font-weight: 400; }
  .spine-author .last { font-weight: 800; }

  .front-cover {
    position: absolute; left: 632px; top: 134px; width: 568px; height: 904px;
    overflow: hidden;
  }
  .cover-photo {
    position: absolute; inset: 0;
    background:
      radial-gradient(ellipse 70% 30% at 65% 92%, var(--glow) 0%, rgba(242,210,122,0) 70%),
      linear-gradient(180deg, var(--sky-top) 0%, #a9b3b8 18%, var(--sky-mid) 45%, #e6e3d4 68%, #a99a5a 86%, var(--ground) 100%);
  }
  .front-title {
    position: absolute; left: 0; width: 568px; text-align: center;
    font-family: "Dosis", sans-serif; line-height: 1;
  }
  .title-top {
    top: 48px; font-size: 104px; font-weight: 400; color: var(--ink); letter-spacing: 1px;
  }
  .title-main {
    top: 156px; font-size: 138px; font-weight: 500; color: var(--title-blue); letter-spacing: 2px;
  }
  .subtitle {
    position: absolute; left: 0; top: 300px; width: 568px; text-align: center;
    font-family: "Signika", sans-serif; font-weight: 400; font-size: 24px; line-height: 24.5px;
    color: var(--ink); letter-spacing: 0.5px;
  }
  .front-author {
    position: absolute; left: 0; top: 833px; width: 568px; text-align: center;
    font-family: "Open Sans", sans-serif; font-size: 38px; line-height: 1;
    color: var(--white); letter-spacing: 3px;
  }
  .front-author .first { font-weight: 300; margin-right: 12px; }
  .front-author .last { font-weight: 800; }
</style>
</head>
<body>
<main class="spread">
  <section class="back-cover">
    <div class="back-copy">
      <p><span class="lead">Lorem ipsum</span> dolor sit amet, consectetur adipiscing elit, sed do eiusmod tempor incididunt ut labore et dolore magna aliqua. Ut enim ad minim veniam, quis nostrud exercitation ullamco laboris nisi ut aliquip ex ea commodo consequat. Duis aute irure dolor in reprehenderit in voluptate velit esse cillum dolore eu fugiat nulla pariatur. Excepteur sint occaecat cupidatat non proident, sunt in culpa qui officia deserunt mollit anim id est laborum.</p>
      <p>Lorem ipsum dolor sit amet, consectetur adipiscing elit, sed do eiusmod tempor incididunt ut labore et dolore magna aliqua. Ut enim ad minim veniam, quis nostrud exercitation ullamco laboris nisi ut aliquip ex ea commodo consequat. Duis aute irure dolor in reprehenderit in voluptate velit esse cillum dolore eu fugiat nulla pariatur.</p>
    </div>
    <div class="author-band">
      <h2>About the Author</h2>
      <p>Lorem ipsum dolor sit amet, consectetur adipiscing elit, sed do eiusmod tempor incididunt ut labore et dolore magna aliqua. Ut enim ad minim veniam, quis nostrud exercitation ullamco laboris nisi ut aliquip ex ea commodo consequat. Duis aute irure dolor in reprehenderit in voluptate velit esse cillum dolore eu fugiat nulla</p>
    </div>
    <div class="barcode-area"></div>
  </section>

  <section class="spine">
    <div class="spine-text spine-title">FIND YOUR <span class="accent">MENTOR</span></div>
    <div class="spine-text spine-author"><span class="first">DALTON</span> <span class="last">REEVE</span></div>
  </section>

  <section class="front-cover">
    <div class="cover-photo" role="img" aria-label="Photo of a caped hero silhouette standing on a hilltop at sunrise above a hazy city"></div>
    <h1>
      <span class="front-title title-top">FIND YOUR</span>
      <span class="front-title title-main">MENTOR</span>
    </h1>
    <p class="subtitle">How to fast-track your career through<br>contacting, hearing back from,<br>and making a lasting mark on the<br>leaders you look up to most</p>
    <p class="front-author"><span class="first">DALTON</span><span class="last">REEVE</span></p>
  </section>
</main>
</body>
</html>
```